Need a business card for our overland brand!

We had the logo made and we need a great design for our business card. Use the logo provide or tweak it however you see fit.

Contact Information for Business Card

Name, Title, Telephone, email, website

```html
<!DOCTYPE html>
<html lang="en">
<head>
<meta charset="utf-8">
<title>Tundra Trailworks – Business Card</title>
<link rel="stylesheet" href="https://fonts.googleapis.com/css2?family=Oswald:wght@700&family=Poppins:wght@400&display=swap">
<style>
  :root {
    --navy: #243752;
    --teal: #1f88a8;
    --cyan: #1ea3c9;
    --ink: #1b1f26;
    --paper: #ffffff;
    --mist: #ececee;
    --rule: #c9cdd3;
    --backdrop: #2c2c2c;
  }
  * { margin: 0; padding: 0; box-sizing: border-box; }
  html, body { width: 1200px; height: 866px; overflow: hidden; background: var(--backdrop); }
  .stage { position: relative; width: 1200px; height: 866px; }

  .card {
    position: absolute;
    top: 278px;
    width: 540px;
    height: 309px;
    overflow: hidden;
    box-shadow: 0 10px 24px rgba(0,0,0,.45);
  }
  .card--front { left: 40px; background: var(--paper); }
  .card--back  { left: 620px; }

  .scenery {
    position: absolute;
    left: 0; top: 0;
    width: 540px; height: 280px;
    background: linear-gradient(100deg, var(--mist) 0%, rgba(236,236,238,.6) 45%, rgba(255,255,255,0) 80%);
  }
  .backdrop-art {
    position: absolute; inset: 0;
    background: linear-gradient(135deg, var(--navy) 0%, var(--navy) 45%, var(--teal) 100%);
  }

  .person { position: absolute; left: 30px; top: 96px; }
  .person__name {
    font-family: "Oswald", sans-serif; font-weight: 700;
    font-size: 22px; letter-spacing: .5px; text-transform: uppercase;
    color: var(--navy); line-height: 1.1;
  }
  .person__title {
    font-family: "Poppins", sans-serif; font-size: 13px;
    color: var(--cyan); letter-spacing: .6px;
  }
  .person__rule { width: 210px; height: 1px; background: var(--rule); margin: 8px 0 8px; }
  .contact {
    font-family: "Poppins", sans-serif; font-size: 11.5px; color: var(--ink);
    display: flex; align-items: center; gap: 7px; line-height: 1.6;
  }
  .contact svg { width: 11px; height: 11px; fill: var(--ink); flex: none; }

  .brand {
    position: relative;
    font-family: "Oswald", sans-serif; font-weight: 700;
    text-transform: uppercase; line-height: .95; letter-spacing: 1px;
  }
  .card--front .brand { position: absolute; left: 285px; top: 92px; font-size: 42px; color: var(--navy); }
  .card--back .brand { position: absolute; left: 0; right: 0; top: 100px; text-align: center; font-size: 54px; color: var(--paper); }

  .footer-band { position: absolute; left: 0; bottom: 0; width: 540px; height: 62px; }
  .footer-band__stripe { fill: var(--cyan); }
  .footer-band__base { fill: var(--navy); }
  .website {
    position: absolute; right: 28px; bottom: 9px;
    font-family: "Poppins", sans-serif; font-size: 13px;
    color: var(--paper); letter-spacing: 1.2px;
  }
</style>
</head>
<body>
<main class="stage">

  <section class="card card--front">
    <div class="scenery" role="img" aria-label="Faint grey mountain range illustration"></div>

    <div class="person">
      <p class="person__name">Marcus Hale</p>
      <p class="person__title">Managing Director</p>
      <div class="person__rule"></div>
      <p class="contact">
        <svg viewBox="0 0 16 16" aria-hidden="true"><path d="M3.6 1.2l2.3 2.4-1.3 2.1c.9 2 2.5 3.6 4.6 4.6l2.1-1.3 2.4 2.3-1.4 2.6c-5.6-.4-10-4.8-10.4-10.4z"/></svg>
        044-987 654 321
      </p>
      <p class="contact">
        <svg viewBox="0 0 16 16" aria-hidden="true"><path d="M1 3h14v10H1z M1.8 3.8L8 9l6.2-5.2" fill="none" stroke="#1b1f26" stroke-width="1.6"/></svg>
        hello@tundratrail.com
      </p>
    </div>

    <p class="brand">Tundra<br>Trailworks</p>

    <svg class="footer-band" viewBox="0 0 540 62" aria-hidden="true">
      <path class="footer-band__stripe" d="M0 40 H196 C210 40 212 36 222 36 V42 C214 42 210 46 196 46 H0 Z"/>
      <path class="footer-band__base" d="M0 62 V52 H190 C212 52 214 34 236 34 H540 V62 Z"/>
    </svg>
    <p class="website">www.tundratrail.com</p>
  </section>

  <section class="card card--back">
    <div class="backdrop-art" role="img" aria-label="Deep blue gradient with faint mountain silhouettes"></div>
    <p class="brand">Tundra<br>Trailworks</p>
  </section>

</main>
</body>
</html>
```